Business Card for Bloom Vitality & Strength

Hi can you please design a business card with my logo and program logo (the new one I just sent) somewhere on it too maybe on the back? Needs to be eye catching and super cool.
Marla Quintby, Director
Master Personal Trainer & Nutrition Coach
0412 786 305
Www.bloomvitalitystrength.com.au
Insta (logo) bloom_vitality_strength #bloomyou7x72018

Target Market(s)

30+ women looking to change lifestyle to healthy mind body etc

Industry/Entity Type

Health And Wellness

Contact Information for Business Card

As above

Font styles to use
Sans Serif

Colors

Designer to choose colors to be used in the design.

Requirements
Must have
• Must super cool and edgy with a bit of cuteness

```html
<!DOCTYPE html>
<html lang="en">
<head>
<meta charset="utf-8">
<title>Bloom Vitality &amp; Strength – Business Card</title>
<link rel="stylesheet" href="https://fonts.googleapis.com/css2?family=Lato:wght@400;700;900&display=swap">
<style>
  :root {
    --stage: #000000;
    --card-front: #ffffff;
    --card-back: #efefef;
    --ink: #111111;
    --accent: #b3141b;
    --rule: #cfcfcf;
  }
  html, body {
    margin: 0;
    width: 1200px;
    height: 900px;
    overflow: hidden;
    background: var(--stage);
    font-family: "Lato", sans-serif;
    color: var(--ink);
  }
  .canvas { position: relative; width: 1200px; height: 900px; }

  .card { position: absolute; top: 275px; width: 477px; height: 293px; box-sizing: border-box; }
  .card--front { left: 116px; background: var(--card-front); border-radius: 0 58px 0 58px; }
  .card--back  { left: 622px; background: var(--card-back);  border-radius: 58px 0 58px 0; }

  .brand {
    position: absolute;
    display: flex; align-items: center; gap: 10px;
    font-weight: 900; font-size: 21px; letter-spacing: 0.2px; color: var(--ink);
    white-space: nowrap;
  }
  .brand__dot { width: 18px; height: 18px; border-radius: 50%; background: var(--accent); flex: none; }
  .card--front .brand { right: 26px; top: 70px; }
  .card--back .brand { left: 0; right: 0; justify-content: center; top: 96px; }

  .person { position: absolute; left: 31px; top: 137px; }
  .person__name { margin: 0; font-weight: 700; font-size: 18px; color: var(--accent); text-transform: uppercase; letter-spacing: 0.2px; }
  .person__role { margin: -3px 0 0 -1px; font-size: 13.5px; line-height: 18px; }

  .rule { position: absolute; height: 1px; background: var(--rule); }
  .card--front .rule { left: 31px; right: 25px; top: 201px; }
  .card--back .rule { left: 38px; right: 38px; top: 161px; }

  .contact { position: absolute; left: 30px; top: 207px; margin: 0; padding: 0; list-style: none; font-size: 13.5px; }
  .contact li { display: flex; align-items: center; gap: 4px; height: 18px; }
  .contact li.contact__social { margin-top: 7px; }
  .contact svg { width: 12px; height: 12px; flex: none; }

  .program {
    position: absolute; left: 0; right: 0; top: 200px;
    display: flex; align-items: center; justify-content: center; gap: 8px;
    font-weight: 400; font-size: 19px; letter-spacing: 2px; color: var(--ink);
    white-space: nowrap;
  }
  .program__dot { width: 14px; height: 14px; border-radius: 50%; background: var(--accent); flex: none; }
</style>
</head>
<body>
<div class="canvas">
  <section class="card card--front">
    <div class="brand"><span class="brand__dot"></span>Bloom Vitality &amp; Strength</div>
    <div class="person">
      <h1 class="person__name">Marla Quintby</h1>
      <div class="person__role">Director<br>Master Personal Trainer &amp; Nutrition Coach</div>
    </div>
    <div class="rule"></div>
    <ul class="contact">
      <li>
        <svg viewBox="0 0 12 12" aria-hidden="true"><path fill="#b3141b" d="M1 3.5C1 2 3 1.5 6 1.5S11 2 11 3.5V5H8.5V4h-5v1H1zM3 5.5h6l1.5 4.5h-9z"/></svg>
        0412 786 305
      </li>
      <li>
        <svg viewBox="0 0 12 12" aria-hidden="true"><circle cx="6" cy="6" r="5.5" fill="#b3141b"/><path d="M1 6h10M6 .5c-2.5 3-2.5 8 0 11M6 .5c2.5 3 2.5 8 0 11" stroke="#fff" stroke-width=".8" fill="none"/></svg>
        www.bloomvitalitystrength.com.au
      </li>
      <li class="contact__social">
        <svg viewBox="0 0 12 12" aria-hidden="true"><rect width="12" height="12" rx="2" fill="#b3141b"/></svg>
        bloom_vitality_strength #bloomyou7x72018
      </li>
    </ul>
  </section>

  <section class="card card--back">
    <div class="brand"><span class="brand__dot"></span>Bloom Vitality &amp; Strength</div>
    <div class="rule"></div>
    <div class="program"><span class="program__dot"></span>BloomYou7x7</div>
  </section>
</div>
</body>
</html>
```